Paws Of Kindness Business cards

Design a cool, modern business card for my bully breed rescue.

Contact Information for Business Card

Marlene
517-382-4061 Marlene@PawsOfKindnessRescue.net PawsOfKindnessRescue.net

Font styles to use
Serif
Sans Serif

Colors

Designer to choose colors to be used in the design.

Requirements
Must have
• logo and info. Color
Nice to have
• Foil. Maybe some paw prints on the back or some kind of dog illustration.

```html
<!DOCTYPE html>
<html lang="en">
<head>
<meta charset="utf-8">
<title>Paws Of Kindness – Business Cards</title>
<link href="https://fonts.googleapis.com/css2?family=Montserrat:wght@400;700;800&display=swap" rel="stylesheet">
<style>
  :root{
    --bg:#e9e6e1;
    --card:#ffffff;
    --ink:#1c1c1c;
    --name:#3a3a3a;
    --bar-1:#1f1f1f;
    --bar-2:#2c2c2c;
    --bar-3:#474747;
    --bar-text:#f2f2f2;
    --rule:#555555;
  }
  *{box-sizing:border-box;margin:0;padding:0}
  html,body{width:1200px;height:797px;overflow:hidden}
  body{
    background:var(--bg);
    font-family:"Montserrat",sans-serif;
    position:relative;
  }
  .card{
    position:absolute;
    width:520px;height:297px;
    background:var(--card);
    box-shadow:0 6px 18px rgba(0,0,0,.18);
  }
  .card--front{left:50px;top:250px}
  .card--back{left:630px;top:250px}

  .brand{
    display:flex;align-items:center;gap:12px;
    position:absolute;
  }
  .brand__dot{
    border-radius:50%;
    border:3px solid var(--ink);
    flex:none;
  }
  .brand__name{
    font-weight:800;
    color:var(--ink);
    text-transform:uppercase;
    letter-spacing:.5px;
    white-space:nowrap;
  }
  .card--front .brand{left:50%;top:50%;transform:translate(-50%,-50%)}
  .card--front .brand__dot{width:46px;height:46px}
  .card--front .brand__name{font-size:30px}

  .card--back .brand{left:122px;top:50%;transform:translate(-50%,-50%)}
  .card--back .brand__dot{width:26px;height:26px;border-width:2px}
  .card--back .brand__name{font-size:17px}
  .card--back .brand{gap:8px}

  .divider{
    position:absolute;left:240px;top:38px;
    width:2px;height:220px;background:var(--rule);
  }
  .contact{
    position:absolute;left:246px;top:92px;right:10px;
  }
  .contact__name{
    font-weight:700;font-size:15px;color:var(--name);
    margin:0 0 6px 8px;
  }
  .contact__row{
    display:block;
    height:24px;line-height:24px;
    padding-left:8px;
    font-size:10.5px;color:var(--bar-text);
    white-space:nowrap;
    margin-bottom:3px;
  }
  .contact__row--phone{background:var(--bar-1)}
  .contact__row--email{background:var(--bar-2)}
  .contact__row--web{background:var(--bar-3)}
</style>
</head>
<body>
  <section class="card card--front" aria-label="Card front">
    <div class="brand">
      <span class="brand__dot"></span>
      <span class="brand__name">Paws Of Kindness</span>
    </div>
  </section>

  <section class="card card--back" aria-label="Card back">
    <div class="brand">
      <span class="brand__dot"></span>
      <span class="brand__name">Paws Of Kindness</span>
    </div>
    <div class="divider"></div>
    <div class="contact">
      <p class="contact__name">Marlene</p>
      <span class="contact__row contact__row--phone">Phone: 517-382-4061</span>
      <span class="contact__row contact__row--email">Email: Marlene@PawsOfKindnessRescue.net</span>
      <span class="contact__row contact__row--web">Web: PawsOfKindnessRescue.net</span>
    </div>
  </section>
</body>
</html>
```